Website for our 3rd party logistics warehouse company

Our company is a 3rd party logistics company. We receive and ship other businesses products for them. We offer our services to other smaller businesses that do not have a warehouse to operate out of. We also help many Brindlemart businesses prepare their products to be sold on Brindlemart.

We are looking for a modern looking design for our website. Please see our attached logo for design ideas. We are open to changing logo colors for website.

We really like the look of the website www.quorvane.com

Target Market(s)

Other businesses and brands of products

Industry/Entity Type

Warehousing and shipping

Number of Pages Required

2 page

Requirements
Must have
• We need 2 pages. Our main landing page and a duplicate page with different information geared towards brands.
Nice to have
• I like the look of overlay/transparent sections. Please see quorvane.com there is a ribbon that shows "Partners".

```html
<!DOCTYPE html>
<html lang="en">
<head>
<meta charset="utf-8">
<title>Halvern 3PL — Website Design Board</title>
<link href="https://fonts.googleapis.com/css2?family=Oswald:wght@400;500;600&family=Source+Sans+3:wght@300;400;600&display=swap" rel="stylesheet">
<style>
:root{
  --ink:#1e1e1e;
  --gold:#fec841;
  --steel:#a7a9ac;
  --cream:#fdefc7;
  --paper:#f4f4f4;
  --white:#ffffff;
}
*{box-sizing:border-box;margin:0;padding:0}
html,body{width:1200px;height:3038px;overflow:hidden;background:var(--cream)}
body{font-family:"Source Sans 3",sans-serif;color:var(--ink)}
.board{position:relative;width:1200px;height:3038px;overflow:hidden;background:var(--cream)}
.abs{position:absolute}

/* photo areas: soft gradients in the tones of each photograph */
.photo-warehouse{background:
  linear-gradient(180deg,rgba(0,0,0,.28) 0%,rgba(0,0,0,.12) 40%,rgba(0,0,0,.38) 100%),
  linear-gradient(95deg,#3b3830 0%,#575041 18%,#6e6550 32%,#4a4539 46%,#7a6b45 60%,#b39a4c 70%,#8c7a48 78%,#4e4737 88%,#2d2b26 100%)}
.photo-forklift{background:radial-gradient(ellipse 52% 62% at 58% 52%,#fec841 0%,#f8cf58 40%,#efdc9c 62%,rgba(244,244,244,0) 78%),linear-gradient(90deg,#eeeae0,#f4f4f4)}
.photo-phone{background:radial-gradient(ellipse 45% 55% at 45% 35%,#f1efe8 0%,#c9c2b4 30%,#a88c74 55%,rgba(40,38,34,.6) 80%),linear-gradient(180deg,#2a2926,#151515)}
.photo-pallet{background:linear-gradient(160deg,#e4e0d8 0%,#bdb6aa 28%,#8f887c 46%,#c9a53a 66%,#e4b93c 74%,#7d776c 88%,#5e5a52 100%)}

/* brand header */
.brand-title{position:absolute;left:0;width:1200px;top:140px;text-align:center;font-family:"Oswald",sans-serif;font-weight:500;font-size:34px;letter-spacing:6px;color:var(--ink)}
.spec-label{font-family:"Oswald",sans-serif;font-size:24px;font-weight:500;color:var(--ink)}
.font-sample-a{font-family:"Oswald",sans-serif;font-size:24px;font-weight:500}
.font-sample-b{font-size:14px;color:#444}
.swatch{position:absolute;width:44px;height:44px;border-radius:50%}
.swatch-code{position:absolute;font-size:11px;color:#555;width:60px;text-align:center}

/* flat screens */
.screen{position:absolute;overflow:hidden;box-shadow:0 10px 24px rgba(0,0,0,.18)}
.screen .photo{position:absolute;inset:0}
.screen .bar{position:absolute;left:0;right:0;top:0;background:var(--gold)}
.screen .logo{position:absolute;font-family:"Oswald",sans-serif;font-weight:500;color:var(--white)}
.screen .nav{position:absolute;font-family:"Oswald",sans-serif;color:var(--white);white-space:nowrap}
.screen .nav b{color:var(--gold);font-weight:400}
.screen .kicker{position:absolute;left:0;right:0;text-align:center;color:#ddd;text-transform:uppercase}
.screen .title{position:absolute;left:0;right:0;text-align:center;font-family:"Oswald",sans-serif;font-weight:500;color:var(--white);line-height:1.15}
.screen .btn{position:absolute;background:var(--gold);font-family:"Oswald",sans-serif;color:var(--ink);text-align:center;font-weight:500}

/* desktop site */
.site{position:absolute;left:160px;top:1023px;width:677px;height:1913px;background:var(--white);overflow:hidden}
.sec{position:absolute;left:0;width:100%}
.topbar{background:var(--gold);font-size:6px;display:flex;gap:22px;padding-left:91px;align-items:center}
.hero-photo{position:absolute;inset:0}
.site-logo{font-family:"Oswald",sans-serif;font-weight:500;color:var(--white);font-size:13px;letter-spacing:2px}
.site-nav{font-family:"Oswald",sans-serif;font-size:7px;color:var(--white);display:flex;gap:14px}
.site-nav .active{color:var(--gold)}
.hero-rule{position:absolute;left:0;right:0;top:62px;height:1px;background:rgba(255,255,255,.15)}
.kicker{font-size:6px;letter-spacing:3px;text-transform:uppercase}
.kicker.light{color:#d9d9d9}
.kicker.gold{color:#c79a1d}
.kicker.dim{color:#999}
.h1{font-family:"Oswald",sans-serif;font-weight:500;font-size:30px;color:var(--white)}
.h2{font-family:"Oswald",sans-serif;font-weight:500;font-size:18px;line-height:1.1}
.btn{display:block;background:var(--gold);font-family:"Oswald",sans-serif;font-weight:500;font-size:7px;text-align:center;color:var(--ink)}
.body{font-size:6.5px;line-height:1.9;color:#555}
.body.light{color:#e8e8e8}
.tabs{display:flex;background:rgba(130,130,140,.6)}
.tabs div{flex:1;font-family:"Oswald",sans-serif;font-size:8px;color:var(--gold);display:flex;align-items:center;justify-content:center;border-right:1px solid rgba(255,255,255,.15)}
.tabs div:last-child{border-right:none}
.dark{background:#000}
.light-grey{background:var(--paper)}
.yellow{background:var(--gold)}
.software{background:#151515}
.guarantee{background:var(--steel)}
.footer{background:#151515}
.num{font-family:"Oswald",sans-serif;font-size:14px;color:#d9a72a;border:1px solid #e3c36a;width:22px;height:24px;display:flex;align-items:center;justify-content:center}
.feature-text{font-size:6px;line-height:1.9;color:#666;width:80px}
.perk{position:absolute;width:120px;text-align:center}
.perk svg{display:block;margin:0 auto}
.perk .dash{width:14px;height:1px;background:var(--ink);margin:8px auto 6px}
.perk p{font-family:"Oswald",sans-serif;font-size:6.5px;line-height:1.8;color:var(--ink)}
.field{position:absolute;border:1px solid #e2e2e2;font-size:5.5px;color:#999;padding:7px 8px}
.foot-h{font-family:"Oswald",sans-serif;font-size:10px;color:var(--white)}
.foot-rule{width:16px;height:1px;background:var(--gold)}
.foot-list{font-size:6.5px;line-height:2.7;color:#ccc;list-style:none}
.foot-list .gold{color:var(--gold)}
.copyright{background:var(--gold);font-size:5.5px;text-align:center;display:flex;align-items:center;justify-content:center}
.ph{position:absolute}

/* mobile */
.mobile{position:absolute;left:863px;top:1023px;width:111px;height:1913px;background:var(--white);overflow:hidden}
.m-t{font-size:3.6px;line-height:1.7;color:#666}
.m-t.light{color:#ddd}
.m-h{font-family:"Oswald",sans-serif;font-weight:500;font-size:9px}
.m-k{font-size:3px;letter-spacing:1.5px;text-transform:uppercase}
.m-num{font-family:"Oswald",sans-serif;font-size:7px;color:#d9a72a;border:1px solid #e3c36a;width:11px;height:11px;display:flex;align-items:center;justify-content:center}
.m-field{position:absolute;left:8px;width:95px;border:1px solid #e2e2e2;font-size:3px;color:#999;padding:3px 4px}

.side-label{position:absolute;font-size:18px;letter-spacing:10px;color:var(--ink);font-weight:300;white-space:nowrap}
</style>
</head>
<body>
<div class="board">

  <div class="brand-title">HALVERN 3PL</div>

  <div class="abs spec-label" style="left:322px;top:296px">Fonts:</div>
  <div class="abs font-sample-a" style="left:391px;top:286px">OSWALD</div>
  <div class="abs font-sample-b" style="left:391px;top:324px">Source Sans Pro</div>

  <div class="abs spec-label" style="left:734px;top:298px">Colors:</div>
  <div class="swatch" style="left:809px;top:287px;background:var(--ink)"></div>
  <div class="swatch" style="left:865px;top:287px;background:var(--gold)"></div>
  <div class="swatch" style="left:921px;top:287px;background:var(--steel)"></div>
  <div class="swatch-code" style="left:801px;top:340px">#1e1e1e</div>
  <div class="swatch-code" style="left:857px;top:340px">#fec841</div>
  <div class="swatch-code" style="left:913px;top:340px">#a7a9ac</div>

  <!-- flat screens -->
  <div class="screen" style="left:354px;top:436px;width:586px;height:330px">
    <div class="photo photo-warehouse" role="img" aria-label="Warehouse worker in hard hat and hi-vis vest holding a tablet among shelving"></div>
    <div class="bar" style="height:16px"></div>
    <div class="logo" style="left:78px;top:38px;font-size:10px;letter-spacing:1.5px">HALVERN 3PL</div>
    <div class="nav" style="left:308px;top:40px;font-size:6px;word-spacing:12px"><b>HOME</b> ABOUT WHY&nbsp;3PL BENEFITS SOFTWARE CONTACT</div>
    <div class="kicker" style="top:162px;font-size:6px;letter-spacing:3px">Welcome to Halvern 3PL</div>
    <div class="title" style="top:172px;font-size:25px">3RD PARTY LOGISTICS COMPANY</div>
    <div class="btn" style="left:258px;top:224px;width:70px;height:24px;line-height:24px;font-size:6px">OUR SERVICES</div>
  </div>

  <div class="screen" style="left:161px;top:680px;width:365px;height:228px">
    <div class="photo photo-warehouse" role="img" aria-label="Warehouse worker in hard hat and hi-vis vest holding a tablet among shelving"></div>
    <div class="bar" style="height:10px"></div>
    <div class="logo" style="left:48px;top:24px;font-size:7px;letter-spacing:1px">HALVERN 3PL</div>
    <div class="nav" style="left:192px;top:26px;font-size:4px;word-spacing:7px"><b>HOME</b> ABOUT WHY&nbsp;3PL BENEFITS SOFTWARE CONTACT</div>
    <div class="kicker" style="top:100px;font-size:4px;letter-spacing:2px">Welcome to Halvern 3PL</div>
    <div class="title" style="top:106px;font-size:16px">3RD PARTY LOGISTICS COMPANY</div>
    <div class="btn" style="left:161px;top:138px;width:44px;height:16px;line-height:16px;font-size:4px">OUR SERVICES</div>
    <div class="abs" style="left:48px;top:212px;width:269px;height:16px;background:rgba(130,130,140,.6);display:flex;font-family:Oswald,sans-serif;font-size:4px;color:var(--gold);align-items:center;justify-content:space-around">
      <span>01 - QUICK DELIVERY</span><span>02 - APP TRACKING</span><span>03 - AFFORDABLE PRICING</span>
    </div>
  </div>

  <div class="screen" style="left:896px;top:680px;width:120px;height:234px">
    <div class="photo photo-warehouse" role="img" aria-label="Warehouse worker in hard hat and hi-vis vest among shelving"></div>
    <div class="bar" style="height:10px"></div>
    <div class="logo" style="left:8px;top:32px;font-size:6px">HALVERN 3PL</div>
    <div class="kicker" style="top:128px;font-size:3.5px;letter-spacing:1.5px">Welcome to Halvern 3PL</div>
    <div class="title" style="top:136px;font-size:11px">3RD PARTY<br>LOGISTICS COMPANY</div>
    <div class="btn" style="left:38px;top:180px;width:44px;height:14px;line-height:14px;font-size:3.5px">OUR SERVICES</div>
  </div>

  <div class="side-label" style="left:40px;top:1930px;transform:rotate(-90deg);transform-origin:center;width:190px;text-align:center">LAPTOP / DESKTOP</div>
  <div class="side-label" style="left:935px;top:1925px;transform:rotate(90deg);transform-origin:center;width:135px;text-align:center">RESPONSIVE</div>

  <!-- desktop site -->
  <main class="site">
    <div class="sec topbar" style="top:0;height:18px">
      <span>&#9742; +1 555 010 2040</span><span>&#9993; info@halvern3pl.com</span>
    </div>

    <section class="sec" style="top:18px;height:425px">
      <div class="hero-photo photo-warehouse" role="img" aria-label="Warehouse worker in hard hat and hi-vis vest checking a tablet, colleagues and shelving behind"></div>
      <div class="abs site-logo" style="left:91px;top:24px">HALVERN 3PL</div>
      <nav class="abs site-nav" style="left:356px;top:27px"><span class="active">HOME</span><span>ABOUT</span><span>WHY 3PL</span><span>BENEFITS</span><span>SOFTWARE</span><span>CONTACT</span></nav>
      <div class="hero-rule"></div>
      <div class="abs kicker light" style="left:0;width:677px;text-align:center;top:166px;letter-spacing:4px">Welcome to Halvern 3PL</div>
      <div class="abs h1" style="left:0;width:677px;text-align:center;top:178px">3RD PARTY LOGISTICS COMPANY</div>
      <a class="abs btn" style="left:299px;top:236px;width:80px;height:30px;line-height:30px">OUR SERVICES</a>
      <div class="abs tabs" style="left:91px;top:374px;width:495px;height:51px">
        <div>01 - QUICK DELIVERY</div><div>02 - APP TRACKING</div><div>03 - AFFORDABLE PRICING</div>
      </div>
    </section>

    <section class="sec dark" style="top:443px;height:112px">
      <div class="abs kicker gold" style="left:91px;top:40px">Introduction</div>
      <h2 class="abs h2" style="left:91px;top:52px;color:var(--white)">WHO WE ARE</h2>
      <p class="abs body light" style="left:345px;top:42px;width:245px">Halvern 3PL is your one stop 3PL that will help you grow your business and allow you to be handsoff. We offer high end services, our commitment - guaranteed.</p>
    </section>

    <section class="sec light-grey" style="top:555px;height:306px">
      <div class="abs kicker dim" style="left:91px;top:40px">Features</div>
      <h2 class="abs h2" style="left:91px;top:52px">WHY USE A PREP 3PL?</h2>
      <div class="ph photo-forklift" role="img" aria-label="Yellow forklift carrying a pallet of cardboard boxes in front of a yellow circle" style="left:91px;top:96px;width:218px;height:166px"></div>
      <p class="abs body" style="left:345px;top:42px;width:245px">Lorem ipsum dolor sit amet, consectetur adipiscing elit, sed do eiusmod tempor incididunt ut labore et dolore magna aliqua.</p>
      <div class="abs num" style="left:345px;top:108px">01</div>
      <p class="abs feature-text" style="left:375px;top:104px">Work from anywhere in the world</p>
      <div class="abs num" style="left:477px;top:108px">02</div>
      <p class="abs feature-text" style="left:507px;top:104px">Don't have to manage employees, health insurance plans, payroll, SICK CALLS, ETC</p>
      <div class="abs num" style="left:345px;top:174px">03</div>
      <p class="abs feature-text" style="left:375px;top:170px">Don't get locked warehouse lease where you LOSE hundreds of dollars.</p>
      <div class="abs num" style="left:477px;top:174px">04</div>
      <p class="abs feature-text" style="left:507px;top:170px">Grow your business without commitment</p>
      <p class="abs body" style="left:345px;top:238px;width:245px">Lorem ipsum dolor sit amet, consectetur adipiscing elit, sed do eiusmod tempor incididunt ut labore et dolore magna aliqua.</p>
    </section>

    <section class="sec yellow" style="top:861px;height:159px">
      <div class="perk" style="left:86px;top:42px">
        <svg width="30" height="28" viewBox="0 0 30 28" fill="none" stroke="#1e1e1e" stroke-width="1.4"><path d="M8 10l9-5 9 5v10l-9 5-9-5z"/><path d="M8 10l9 5 9-5M17 15v10"/><path d="M2 14h5M3 18h4"/></svg>
        <div class="dash"></div><p>48 HOUR TURN AROUND GUARANTEE –<br>DONE IN 48 HOURS OR ITS FREE*</p>
      </div>
      <div class="perk" style="left:204px;top:42px">
        <svg width="30" height="28" viewBox="0 0 30 28" fill="none" stroke="#1e1e1e" stroke-width="1.4"><rect x="6" y="3" width="18" height="22" rx="1"/><path d="M10 9h10M10 13h10M10 17h6"/></svg>
        <div class="dash"></div><p>NO MONTHLY SUBSCRIPTION –<br>ONLY PAY FOR WHAT YOU USE</p>
      </div>
      <div class="perk" style="left:296px;top:42px">
        <svg width="30" height="28" viewBox="0 0 30 28" fill="none" stroke="#1e1e1e" stroke-width="1.4"><rect x="5" y="3" width="16" height="20"/><path d="M9 8h8M9 12h8M9 16h5"/><circle cx="22" cy="20" r="5"/></svg>
        <div class="dash"></div><p>NO RECEIVING FEES</p>
      </div>
      <div class="perk" style="left:388px;top:42px">
        <svg width="30" height="28" viewBox="0 0 30 28" fill="none" stroke="#1e1e1e" stroke-width="1.4"><rect x="4" y="4" width="10" height="8"/><rect x="16" y="4" width="10" height="8"/><rect x="4" y="14" width="10" height="8"/><rect x="16" y="14" width="10" height="8"/><path d="M3 25h24"/></svg>
        <div class="dash"></div><p>NO PALLET OR OUTBOUND FEES</p>
      </div>
      <div class="perk" style="left:493px;top:42px">
        <svg width="30" height="28" viewBox="0 0 30 28" fill="none" stroke="#1e1e1e" stroke-width="1.4"><rect x="6" y="7" width="20" height="14"/><path d="M6 7l10 8 10-8"/><path d="M2 12c0-4 2-6 4-6"/></svg>
        <div class="dash"></div><p>EMAIL AND PHONE SUPPORT</p>
      </div>
    </section>

    <section class="sec software" style="top:1020px;height:218px">
      <div class="abs kicker gold" style="left:91px;top:41px">How it works</div>
      <h2 class="abs h2" style="left:91px;top:53px;color:var(--white)">TRY OUR SOFTWARE</h2>
      <p class="abs body light" style="left:91px;top:84px;width:245px">Know what inventory is at our warehouse in real time. Our software allows you to track your inventory and know how your shipment status in real time. Professional software designed specifically for our needs.</p>
      <a class="abs btn" style="left:91px;top:144px;width:80px;height:32px;line-height:32px">DISCOVER MORE</a>
      <div class="ph photo-phone" role="img" aria-label="Hand holding a smartphone showing a delivery tracking map" style="left:451px;top:26px;width:136px;height:192px"></div>
    </section>

    <section class="sec guarantee" style="top:1238px;height:117px">
      <div class="abs kicker" style="left:91px;top:42px;color:#f1f1f1">What we guarantee</div>
      <h2 class="abs h2" style="left:91px;top:55px;color:var(--white)">OUR GUARANTEE:</h2>
      <p class="abs body light" style="left:345px;top:40px;width:250px;color:#f6f6f6">All orders will be prepped and ready for shipment in 48 business hours (often 24 or less) and we guarantee it. We are confident in our services and if we do not fulfill our obligation, we offer a 500 item (up to $700) credit on your next shipment.</p>
    </section>

    <section class="sec" style="top:1355px;height:337px;background:var(--white)">
      <div class="abs kicker gold" style="left:91px;top:42px">Get in touch</div>
      <h2 class="abs h2" style="left:91px;top:55px">CONTACT US</h2>
      <div class="ph photo-pallet" role="img" aria-label="Worker pulling a yellow pallet jack in a warehouse" style="left:93px;top:98px;width:195px;height:195px"></div>
      <p class="abs body" style="left:345px;top:42px;width:245px">Please fill the form below and we will do our very best to get back at you as soon as possible. Already looking forward to hearing from you.</p>
      <div class="field" style="left:345px;top:97px;width:116px;height:24px">First Name*</div>
      <div class="field" style="left:470px;top:97px;width:116px;height:24px">Phone Number*</div>
      <div class="field" style="left:345px;top:130px;width:116px;height:24px">Email Address*</div>
      <div class="field" style="left:470px;top:130px;width:116px;height:24px">Subject*</div>
      <div class="field" style="left:345px;top:163px;width:241px;height:85px">Message*</div>
      <a class="abs btn" style="left:345px;top:263px;width:80px;height:30px;line-height:30px">SEND YOUR MESSAGE</a>
    </section>

    <footer class="sec footer" style="top:1692px;height:197px">
      <div class="abs site-logo" style="left:91px;top:92px">HALVERN 3PL</div>
      <div class="abs" style="left:241px;top:42px"><div class="foot-h">QUICK LINKS</div><div class="foot-rule" style="margin:22px 0 10px"></div>
        <ul class="foot-list"><li>Home</li><li>About Us</li><li>Why 3PL</li><li>Software</li></ul></div>
      <div class="abs" style="left:380px;top:42px"><div class="foot-h">INFORMATION</div><div class="foot-rule" style="margin:22px 0 10px"></div>
        <ul class="foot-list"><li>Sitemap</li><li>Terms &amp; Conditions</li><li>Privacy Policy</li><li>Disclaimer</li></ul></div>
      <div class="abs" style="left:525px;top:42px"><div class="foot-h">CONTACT</div><div class="foot-rule" style="margin:22px 0 10px"></div>
        <ul class="foot-list"><li class="gold">Email Us At:</li><li>info@halvern3pl.com</li><li class="gold">Need Help?</li><li>+1 555 010 2041</li></ul></div>
    </footer>
    <div class="sec copyright" style="top:1889px;height:24px">Copyright 2021 © Halvern 3PL - All Rights Reserved</div>
  </main>

  <!-- responsive site -->
  <aside class="mobile">
    <div class="sec" style="top:0;height:9px;background:var(--gold);font-size:3px;padding:2px 0 0 8px">&#9742; +1 555 010 2040 &nbsp; &#9993; info@halvern3pl.com</div>
    <section class="sec" style="top:9px;height:245px">
      <div class="hero-photo photo-warehouse" role="img" aria-label="Warehouse worker in hard hat and hi-vis vest"></div>
      <div class="abs" style="left:8px;top:16px;font-family:Oswald,sans-serif;font-size:6px;color:#fff">HALVERN 3PL</div>
      <div class="abs" style="left:98px;top:16px;width:6px;height:5px;border-top:1px solid var(--gold);border-bottom:1px solid var(--gold)"></div>
      <div class="abs m-k" style="left:0;width:111px;text-align:center;top:86px;color:#ddd">Welcome to Halvern 3PL</div>
      <div class="abs" style="left:0;width:111px;text-align:center;top:93px;font-family:Oswald,sans-serif;font-size:10px;color:#fff;line-height:1.25">3RD PARTY<br>LOGISTICS COMPANY</div>
      <a class="abs btn" style="left:33px;top:124px;width:45px;height:14px;line-height:14px;font-size:3px">OUR SERVICES</a>
    </section>
    <div class="sec" style="top:254px;height:87px;background:#b9bac0;font-family:Oswald,sans-serif;font-size:4px;color:var(--gold);text-align:center;line-height:29px">01 - QUICK DELIVERY<br>02 - APP TRACKING<br>03 - AFFORDABLE PRICING</div>
    <section class="sec dark" style="top:341px;height:90px">
      <div class="abs m-k" style="left:7px;top:20px;color:#c79a1d">Introduction</div>
      <div class="abs m-h" style="left:7px;top:26px;color:#fff">WHO WE ARE</div>
      <p class="abs m-t light" style="left:7px;top:42px;width:97px">Halvern 3PL is your one stop 3PL that will help you grow your business and allow you to be handsoff. We offer high end services, our commitment - guaranteed.</p>
    </section>
    <section class="sec light-grey" style="top:431px;height:300px">
      <div class="abs m-k" style="left:7px;top:20px;color:#999">Features</div>
      <div class="abs m-h" style="left:7px;top:26px">WHY USE A PREP 3PL?</div>
      <p class="abs m-t" style="left:7px;top:41px;width:97px">Lorem ipsum dolor sit amet, consectetur adipiscing elit, sed do eiusmod tempor incididunt ut labore.</p>
      <div class="ph photo-forklift" role="img" aria-label="Yellow forklift with a pallet of boxes" style="left:7px;top:64px;width:97px;height:74px"></div>
      <div class="abs m-num" style="left:7px;top:147px">01</div><p class="abs m-t" style="left:22px;top:148px;width:80px">Work from anywhere in the world</p>
      <div class="abs m-num" style="left:7px;top:170px">02</div><p class="abs m-t" style="left:22px;top:168px;width:80px">Don't have to manage employees, health insurance plans, payroll, SICK CALLS, ETC</p>
      <div class="abs m-num" style="left:7px;top:194px">03</div><p class="abs m-t" style="left:22px;top:193px;width:80px">Don't get locked warehouse lease where you lose hundreds of dollars.</p>
      <div class="abs m-num" style="left:7px;top:218px">04</div><p class="abs m-t" style="left:22px;top:220px;width:80px">Grow your business without commitment</p>
      <p class="abs m-t" style="left:7px;top:240px;width:97px">Lorem ipsum dolor sit amet, consectetur adipiscing elit, sed do eiusmod tempor incididunt ut labore.</p>
    </section>
    <section class="sec yellow" style="top:731px;height:270px;font-family:Oswald,sans-serif;font-size:3.4px;text-align:center;line-height:1.6">
      <div class="abs" style="left:0;width:111px;top:20px"><svg width="16" height="14" viewBox="0 0 30 28" fill="none" stroke="#1e1e1e" stroke-width="2"><rect x="4" y="4" width="10" height="8"/><rect x="16" y="4" width="10" height="8"/><rect x="4" y="14" width="10" height="8"/><rect x="16" y="14" width="10" height="8"/></svg><br>NO PALLET OR OUTBOUND FEES</div>
      <div class="abs" style="left:0;width:111px;top:64px"><svg width="16" height="14" viewBox="0 0 30 28" fill="none" stroke="#1e1e1e" stroke-width="2"><rect x="5" y="3" width="16" height="20"/><circle cx="22" cy="20" r="5"/></svg><br>NO RECEIVING FEES</div>
      <div class="abs" style="left:0;width:111px;top:108px"><svg width="16" height="14" viewBox="0 0 30 28" fill="none" stroke="#1e1e1e" stroke-width="2"><rect x="6" y="3" width="18" height="22"/><path d="M10 9h10M10 13h10"/></svg><br>NO MONTHLY SUBSCRIPTION –<br>ONLY PAY FOR WHAT YOU USE</div>
      <div class="abs" style="left:0;width:111px;top:156px"><svg width="16" height="14" viewBox="0 0 30 28" fill="none" stroke="#1e1e1e" stroke-width="2"><path d="M8 10l9-5 9 5v10l-9 5-9-5z"/></svg><br>48 HOUR TURN AROUND GUARANTEE –<br>DONE IN 48 HOURS OR ITS FREE*</div>
      <div class="abs" style="left:0;width:111px;top:206px"><svg width="16" height="14" viewBox="0 0 30 28" fill="none" stroke="#1e1e1e" stroke-width="2"><rect x="6" y="7" width="20" height="14"/><path d="M6 7l10 8 10-8"/></svg><br>EMAIL AND PHONE SUPPORT</div>
    </section>
    <section class="sec software" style="top:1001px;height:248px">
      <div class="abs m-k" style="left:0;width:111px;text-align:center;top:20px;color:#c79a1d">How it works</div>
      <div class="abs m-h" style="left:0;width:111px;text-align:center;top:26px;color:#fff">TRY OUR SOFTWARE</div>
      <p class="abs m-t light" style="left:8px;top:42px;width:95px;text-align:center">Know what inventory is at our warehouse in real time. Our software allows you to track your inventory and shipment status in real time.</p>
      <a class="abs btn" style="left:33px;top:72px;width:45px;height:14px;line-height:14px;font-size:3px">DISCOVER MORE</a>
      <div class="ph photo-phone" role="img" aria-label="Hand holding a smartphone with a tracking map" style="left:20px;top:96px;width:72px;height:152px"></div>
    </section>
    <section class="sec" style="top:1249px;height:106px;background:#ececee">
      <div class="abs m-k" style="left:7px;top:16px;color:#999">What we guarantee</div>
      <div class="abs m-h" style="left:7px;top:22px">OUR GUARANTEE:</div>
      <p class="abs m-t" style="left:7px;top:38px;width:97px">All orders will be prepped and ready for shipment in 48 business hours and we guarantee it. If we do not fulfill our obligation, we offer a credit on your next shipment.</p>
    </section>
    <section class="sec" style="top:1355px;height:357px;background:#fff">
      <div class="abs m-h" style="left:8px;top:22px">CONTACT US</div>
      <p class="abs m-t" style="left:8px;top:38px;width:95px">Please fill the form below and we will do our very best to get back at you as soon as possible. Already looking forward to hearing from you.</p>
      <div class="m-field" style="top:64px;height:12px">First Name</div>
      <div class="m-field" style="top:82px;height:12px">Email Address</div>
      <div class="m-field" style="top:100px;height:12px">Phone Number</div>
      <div class="m-field" style="top:118px;height:12px">Subject</div>
      <div class="m-field" style="top:136px;height:50px">Message</div>
      <a class="abs btn" style="left:8px;top:200px;width:45px;height:14px;line-height:14px;font-size:3px">SEND YOUR MESSAGE</a>
      <div class="ph photo-pallet" role="img" aria-label="Worker pulling a yellow pallet jack" style="left:8px;top:240px;width:95px;height:95px"></div>
    </section>
    <footer class="sec footer" style="top:1712px;height:189px">
      <div class="abs" style="left:7px;top:28px;font-family:Oswald,sans-serif;font-size:5px;color:#fff">HALVERN 3PL</div>
      <div class="abs" style="left:64px;top:22px;font-family:Oswald,sans-serif;font-size:5px;color:#fff">QUICK LINKS</div>
      <ul class="abs foot-list" style="left:64px;top:38px;font-size:3.2px;line-height:2.6"><li>Home</li><li>About Us</li><li>Why 3PL</li><li>Software</li></ul>
      <div class="abs" style="left:7px;top:102px;font-family:Oswald,sans-serif;font-size:5px;color:#fff">INFORMATION</div>
      <ul class="abs foot-list" style="left:7px;top:116px;font-size:3.2px;line-height:2.6"><li>Sitemap</li><li>Terms &amp; Conditions</li><li>Privacy Policy</li><li>Disclaimer</li></ul>
      <div class="abs" style="left:64px;top:102px;font-family:Oswald,sans-serif;font-size:5px;color:#fff">CONTACT</div>
      <ul class="abs foot-list" style="left:64px;top:116px;font-size:3.2px;line-height:2.6"><li class="gold">Email Us At:</li><li>info@halvern3pl.com</li><li class="gold">Need Help?</li><li>+1 555 010 2041</li></ul>
    </footer>
    <div class="sec copyright" style="top:1901px;height:12px;font-size:3px">Copyright 2021 © Halvern 3PL - All Rights Reserved</div>
  </aside>

</div>
</body>
</html>
```